Stationery for London Estate Agents (Real Estate)

We are a modern and professional Estate Agency (Realtors) working with high quality properties in London.
We wish to redesign our stationary using our branding displayed on the front of our offices and require a digital version of this logo to be produced (photograph attached). Slight 'tweaking' of this branding is acceptable.
Updates
1st July 2010 Thank you all those designers who have uploaded submissions. Business Card - Details Side: Business Card - Logo Side: Outline of London Skyline Examples of the london skyline are available at http://www.pictovantix.com/searchkwy_london-skyline-silhouette Please be advised that we are looking for an outline, not a 'filled in' silhouette. Letterhead Please feel free to ask us any questions. Bertrand
I have been able to further refine our design requirements based on your submissions.
We like Pale Forks' business card submission that has not been eliminated and have the following design clarifications;
a) Please use an email icon (e.g an envelope).
b) Please make the email as equally prominent as the telephone and fax
c) We very much like VelloTrine's 'mini window icon' - please display the website URL under such a mini window icon at the bottom right of the card.
We are very happy with the colouring, fonts and proportions used by Pale Forks.
We invite designers to try adding an outline of the London Skyline to the left of the large window icon on the business card and in a suitablie position on the Letterhead (e.g at the top left of the letterhead).
We have the following design clarifiications to our Letterhead requirements;
A) We would like the main logo to be on the top right side of the letterhead.
B) We do NOT want the large window icon to be on the left of the logo or the bottom of the letterhead. We are happy having the large window icon to the right or underneath the KB brand.
C) Please use icons for tel, fax and email (e.g. envelope icon for e-mail address)
D) We like two coloured red borders, one at the top and bottom of the letterhead but are happy for variations in shape and size.
E) We currently prefer our address and contact details at the bottom of the letterhead.
F) We like VelloTrine's 'mini window icon' and would prefer this to be used to display the website URL at the bottom right of the letterhead.
G) Please be advised that the letterhead does NOT need additional space for the Company Name as per Pale Forks' submission - the KB brand is sufficient.
Target Market(s)
Owners of high quality property in London.
Industry/Entity Type
Real Estate
Requirements
Must have
- Business Cards: We would like a 'vertical' style business card with our branding on one side and our staff's details on the other;
- Our website is www.korbend.com and we are flexible where that should be on the card and letterhead.
- Stationery details are available in a file attached to this project.
Nice to have
- It would be great to have a horizontal version of the digital logo for placement on property portals (150x60)
Should not have
- Logo should not deviate significantly from the branding on our offices (shop front) - photograph attached.

```html
<!DOCTYPE html>
<html lang="en">
<head>
<meta charset="utf-8">
<title>Korbend Residential – Stationery</title>
<link href="https://fonts.googleapis.com/css2?family=Arimo:wght@400;700&display=swap" rel="stylesheet">
<style>
  :root {
    --plum: #990073;
    --sun: #fff21a;
    --paper: #ffffff;
  }
  * { box-sizing: border-box; margin: 0; padding: 0; }
  html, body { width: 849px; height: 1200px; overflow: hidden; background: var(--paper); }
  body { font-family: "Arimo", Arial, sans-serif; }
  .sheet { position: relative; width: 849px; height: 1200px; background: var(--paper); overflow: hidden; }

  /* letterhead header */
  .header-band { position: absolute; left: 0; top: 0; width: 849px; height: 104px; }
  .header-brand { position: absolute; left: 78px; top: 34px; color: var(--paper); font-size: 25px; line-height: 1; text-align: center; letter-spacing: .5px; }
  .header-brand span { display: block; font-size: 22px; letter-spacing: 2px; margin-top: 2px; }
  .header-services { position: absolute; right: 34px; top: 15px; color: var(--paper); font-size: 15px; }
  .company-reg { position: absolute; left: 487px; top: 78px; color: var(--plum); font-size: 11px; font-weight: 700; }

  /* business cards */
  .card { position: absolute; width: 223px; height: 344px; background: var(--plum); color: var(--paper); text-align: center; }
  .card--front-a { left: 194px; top: 261px; }
  .card--front-b { left: 451px; top: 261px; }
  .card--back { left: 194px; top: 622px; }
  .card--back-light { left: 451px; top: 622px; background: var(--paper); border: 1.5px solid var(--plum); color: var(--plum); }

  .card-brand { position: absolute; left: 0; right: 0; top: 30px; font-size: 23px; line-height: 1; letter-spacing: .5px; }
  .card-brand span { display: block; font-size: 21px; letter-spacing: 2px; margin-top: 3px; }
  .card-services { position: absolute; left: 0; right: 0; top: 103px; font-size: 7.5px; }
  .card-mark { position: absolute; right: 18px; bottom: 20px; width: 50px; height: 50px; background: var(--sun); }

  .card-name { position: absolute; left: 0; right: 0; top: 112px; font-size: 17px; }
  .card-mobile { position: absolute; left: 0; right: 0; top: 134px; font-size: 13px; color: var(--sun); display: flex; justify-content: center; align-items: center; gap: 3px; }
  .card--back-light .card-mobile { color: var(--plum); }
  .card-details { position: absolute; left: 15px; top: 200px; text-align: left; color: var(--sun); }
  .card--back-light .card-details { color: var(--plum); }
  .card-address { font-size: 10px; line-height: 15px; margin-bottom: 5px; }
  .contact-line { display: flex; align-items: center; gap: 4px; font-size: 12px; line-height: 20px; }
  .card-web { position: absolute; right: 10px; bottom: 8px; text-align: right; font-size: 9px; }
  .card-web .mini-mark { display: block; width: 18px; height: 18px; margin: 0 6px 3px auto; background: var(--plum); }
  .card--back .card-web .mini-mark { background: var(--paper); }

  .icon { width: 11px; height: 11px; fill: currentColor; flex: none; }

  /* letterhead footer */
  .footer-band { position: absolute; left: 0; top: 1116px; width: 849px; height: 84px; background: var(--plum); color: var(--paper); }
  .footer-address { position: absolute; left: 36px; top: 24px; font-size: 17px; }
  .footer-contacts { position: absolute; left: 36px; top: 48px; display: flex; gap: 22px; font-size: 13px; color: var(--sun); }
  .footer-contacts .contact-line { font-size: 13px; }
  .footer-web { position: absolute; right: 14px; bottom: 8px; font-size: 17px; text-align: right; }
  .footer-web .mini-mark { display: block; width: 40px; height: 38px; margin: 0 10px 6px auto; background: var(--sun); }
</style>
</head>
<body>
<svg width="0" height="0" style="position:absolute" aria-hidden="true">
  <symbol id="ico-phone" viewBox="0 0 12 12"><path d="M1 4.5 Q6 1 11 4.5 L10 6 8 5.5 7.5 4.5 H4.5 L4 5.5 2 6Z"/><rect x="2.5" y="6" width="7" height="5" rx="1"/></symbol>
  <symbol id="ico-fax" viewBox="0 0 12 12"><rect x="3" y="1" width="6" height="4"/><rect x="1" y="5" width="10" height="6" rx="1"/></symbol>
  <symbol id="ico-mail" viewBox="0 0 12 12"><path d="M1 2.5h10v7H1z M1.8 3.3 6 6.6 10.2 3.3" fill="none" stroke="currentColor" stroke-width="1.3"/></symbol>
  <symbol id="ico-mobile" viewBox="0 0 12 12"><rect x="3" y="0.5" width="6" height="11" rx="1.2" fill="none" stroke="currentColor" stroke-width="1.3"/><rect x="4.3" y="2" width="3.4" height="5"/></symbol>
</svg>

<main class="sheet">
  <svg class="header-band" viewBox="0 0 849 104" aria-hidden="true">
    <path d="M0 0H849V50H385C345 50 330 40 318 60 C305 85 300 104 270 104 H0Z" fill="var(--plum)"/>
  </svg>
  <div class="header-brand">Korbend<span>Residential</span></div>
  <p class="header-services">Lettings * Sales * Management * Investments</p>
  <p class="company-reg">Company Name &amp; Registration Number</p>

  <section class="card card--front-a">
    <div class="card-brand">KORBEND<span>Residential</span></div>
    <p class="card-services">Lettings * Sales * Management * Investments</p>
    <div class="card-mark"></div>
  </section>

  <section class="card card--front-b">
    <div class="card-brand">KORBEND<span>Residential</span></div>
    <p class="card-services">Lettings * Sales * Management * Investments</p>
    <div class="card-mark"></div>
  </section>

  <section class="card card--back">
    <div class="card-brand">KORBEND<span>Residential</span></div>
    <p class="card-name">Bertrand Osley</p>
    <p class="card-mobile"><svg class="icon"><use href="#ico-mobile"/></svg>07700 900 418</p>
    <div class="card-details">
      <p class="card-address">214 Arden Road,<br>Hampstead, London NW3 9QX</p>
      <p class="contact-line"><svg class="icon"><use href="#ico-phone"/></svg>020 7946 0321</p>
      <p class="contact-line"><svg class="icon"><use href="#ico-fax"/></svg>020 7946 0588</p>
      <p class="contact-line"><svg class="icon"><use href="#ico-mail"/></svg>bertrand@korbend.com</p>
    </div>
    <div class="card-web"><span class="mini-mark"></span>www.korbend.com</div>
  </section>

  <section class="card card--back-light">
    <div class="card-brand">KORBEND<span>Residential</span></div>
    <p class="card-name">Bertrand Osley</p>
    <p class="card-mobile"><svg class="icon"><use href="#ico-mobile"/></svg>07700 900 418</p>
    <div class="card-details">
      <p class="card-address">214 Arden Road,<br>Hampstead, London NW3 9QX</p>
      <p class="contact-line"><svg class="icon"><use href="#ico-phone"/></svg>020 7946 0321</p>
      <p class="contact-line"><svg class="icon"><use href="#ico-fax"/></svg>020 7946 0588</p>
      <p class="contact-line"><svg class="icon"><use href="#ico-mail"/></svg>bertrand@korbend.com</p>
    </div>
    <div class="card-web"><span class="mini-mark"></span>www.korbend.com</div>
  </section>

  <footer class="footer-band">
    <p class="footer-address">214 Arden Road, Hampstead, London NW3 9QX</p>
    <div class="footer-contacts">
      <p class="contact-line"><svg class="icon"><use href="#ico-phone"/></svg>020 7946 0321</p>
      <p class="contact-line"><svg class="icon"><use href="#ico-fax"/></svg>020 7946 0588</p>
      <p class="contact-line"><svg class="icon"><use href="#ico-mail"/></svg>info@korbend.com</p>
    </div>
    <div class="footer-web"><span class="mini-mark"></span>www.korbend.com</div>
  </footer>
</main>
</body>
</html>
```